Rock band business card design

I need an edgy double sided business card to hand out at music events and to send out to radio.

It needs to display our logo, web address and social media icons (linkora, plumbit, vostramesh).

Colour scheme to match our website (www.thedrelliq.com)

Please include this quote:
The clock is turning... a reckoning... THE DRELLIQ.

Logo files have been attached.

I look forward to seeing your designs!

Target Market(s)

radio stations, music fans.

Industry/Entity Type

Events

Requirements
Must have
• Website address, social media icons, quote, colour scheme to match www.thedrelliq.com

```html
<!DOCTYPE html>
<html lang="en">
<head>
<meta charset="utf-8">
<title>THE DRELLIQ – Business Card</title>
<link href="https://fonts.googleapis.com/css2?family=Cinzel:wght@400;500&family=Tinos:ital,wght@0,400;1,400&display=swap" rel="stylesheet">
<style>
  :root {
    --stage: #1c1c1c;
    --umber: #2b1a11;
    --umber-deep: #1e120b;
    --paper: #f7f7f5;
    --ink: #141414;
    --cream: #fbf6ee;
    --sand-light: #f3dfae;
    --sand: #c68a46;
    --clay: #7a4a26;
    --chip: #4a2e1d;
  }
  * { box-sizing: border-box; margin: 0; padding: 0; }
  html, body { width: 1200px; height: 900px; overflow: hidden; }
  body {
    background: var(--stage);
    display: flex;
    flex-direction: column;
    align-items: center;
    justify-content: center;
    gap: 40px;
  }
  .card {
    width: 700px;
    height: 400px;
    position: relative;
    overflow: hidden;
    box-shadow: 0 12px 30px rgba(0,0,0,.5);
  }

  /* Back side */
  .card--back { display: flex; background: var(--paper); }
  .card__sidebar {
    width: 250px;
    background: var(--umber);
    color: var(--cream);
    display: flex;
    flex-direction: column;
    align-items: flex-end;
    padding: 28px 24px 26px 20px;
  }
  .quote {
    font-family: "Tinos", "Times New Roman", serif;
    font-style: italic;
    font-size: 15px;
    line-height: 1.25;
    text-align: right;
  }
  .quote__sign { font-style: normal; display: block; }
  .socials {
    list-style: none;
    margin-top: 32px;
    margin-right: -24px;
    background: var(--chip);
    padding: 12px 14px;
    border-radius: 6px 0 0 6px;
    display: flex;
    flex-direction: column;
    gap: 12px;
  }
  .socials__item {
    display: flex;
    align-items: center;
    gap: 8px;
    font-family: "Tinos", "Times New Roman", serif;
    font-size: 14px;
    color: var(--cream);
  }
  .socials__item::before {
    content: "";
    width: 14px;
    height: 14px;
    background: var(--cream);
  }
  .website {
    margin-top: auto;
    font-family: "Tinos", "Times New Roman", serif;
    font-size: 17px;
    color: var(--cream);
  }
  .card__face {
    flex: 1;
    display: flex;
    align-items: center;
    justify-content: center;
  }
  .wordmark {
    font-family: "Cinzel", "Times New Roman", serif;
    font-weight: 500;
    font-size: 50px;
    letter-spacing: 1px;
    color: var(--ink);
  }

  /* Front side */
  .card--front { color: #fff; }
  .card__scene {
    position: absolute;
    inset: 0;
    background:
      linear-gradient(180deg, rgba(30,18,11,0) 35%, var(--umber-deep) 95%),
      radial-gradient(ellipse at 22% 8%, var(--sand-light) 0%, var(--sand) 32%, var(--clay) 62%, var(--umber) 100%);
  }
  .card__title {
    position: absolute;
    left: 0; right: 0;
    top: 245px;
    text-align: center;
  }
  .card__title .wordmark { color: #fff; font-size: 68px; display: block; line-height: 1; }
  .tagline {
    margin-top: 12px;
    font-family: "Tinos", "Times New Roman", serif;
    font-size: 16px;
    color: var(--cream);
  }
</style>
</head>
<body>
  <section class="card card--back">
    <aside class="card__sidebar">
      <p class="quote">The clock is turning...<br>a reckoning...<span class="quote__sign">THE DRELLIQ.</span></p>
      <ul class="socials">
        <li class="socials__item">linkora</li>
        <li class="socials__item">plumbit</li>
        <li class="socials__item">vostramesh</li>
      </ul>
      <p class="website">www.thedrelliq.com</p>
    </aside>
    <div class="card__face">
      <h1 class="wordmark">THE DRELLIQ</h1>
    </div>
  </section>

  <section class="card card--front">
    <div class="card__scene" role="img" aria-label="Desert pyramids under a glowing golden sunrise sky"></div>
    <div class="card__title">
      <h2 class="wordmark">THE DRELLIQ</h2>
      <p class="tagline">The clock is turning... a reckoning... THE DRELLIQ.</p>
    </div>
  </section>
</body>
</html>
```